Hotdogs & Burgers restaurant needs a new menu design

We need a new menu design for our restaurant "Wurmelo". Wurmelo is a fast food specialized in hotdogs and burgers.We are looking for a simple easy menu design that walk through our customer to order the sandwich ==> the fries =>> the sides and the drinks. Wurmelo Menu:* Sandwiches**Hotdogs Our special fresh grilled hotdog served on fresh buns (Regular – 1.300 OMR / Franks – 2.000 OMR)*** DoganzaLettuce, tomato, jalapeno, pickle, onion, corn, chips, cheese, ketchup, mayo, mustard*** PepperBell pepper, onion, sweet chili sauce, avocado*** Chili FlamesChili carne, cheddar cheese, honey mustard*** ChicagoTomato, pickle, red onion, sweet relish, mustard*** New YorkGrilled onion, beef bacon, barbecue sauce, chili mustard*** Egg & CheeseOmelet, cheese, ketchup, mayo, mustard** Burgers 100% all natural beef & freshly ground, 100 grams each patty served on fresh buns.(Single patty - 2.000 OMR / double patty - 2.500 OMR)*** Sweet Beef BurgerBeef bacon, cheese, lettuce, tomato, pickle.*** Cheese Beef BurgerCheese, pickle, Wurmelo sauce.*** Mexican Beef BurgerGuacamole sauce, red onion, lettuce, tomato, Wurmelo sauce.*** Chicken BurgerFried chicken patty, lettuce, tomato, ranch sauce, Wurmelo sauce== ToppingsExtra veggies 0.100 OMRExtra cheese 0.200 OMRExtra beef Bacon 0.400 OMRExtra patty 0.500 OMR*Fries**Regular 0.600 OMR**Crispy 0.800 OMR**Wedges 0.800 OMR**Chili fries 1.500 OMRTopped with our chili carne, cheddar cheese, jalapeno, honey mustard**Lava fries 1.500 OMRTopped with fried bacon, fried onion, cheddar cheese, ranch sauce*Sides**Crispy strips 1.800 OMR5 pieces of chicken strips topped with BBQ sauce or honey mustard sauce, Wurmelo side sauce**Jalapeno cheese balls 1.300 OMR6 pieces of jalapeno cheese balls, sweet chili side sauce**Nachos 1.500 OMRA plate of nachos topped with cheddar cheese and jalapeno*Drinks**Flavored sparkling cans 0.800 OMR **Fresh orange juice 1.400 OMR**Mineral water 0.300 OMR**Soft drink 0.400 OMR**Mojito 1.500 OMRThe menu should not have any of our products pictures (icons/symbols proffered). we would prefer if the designs have unique icons/symbols created for Wurmelo. you can check our Instagram page https://www.snapfolio.example/wurmelo.official/

Industry/Entity Type

American Restaurant

Colors

Designer to choose colors to be used in the design.

Requirements
Must have
• Wurmelo Logo, Icons

```html
<!DOCTYPE html>
<html lang="en">
<head>
<meta charset="utf-8">
<title>Wurmelo Menu</title>
<link href="https://fonts.googleapis.com/css2?family=Anton&family=Oswald:wght@400;500;600&family=Dancing+Script:wght@500&display=swap" rel="stylesheet">
<style>
  :root {
    --backdrop: #b0afb4;
    --paper: #ffffff;
    --ink: #2b2a26;
    --red: #8a1c1c;
    --red-soft: #c98a8a;
    --yellow: #e3cf1c;
  }
  * { margin: 0; padding: 0; box-sizing: border-box; }
  html, body { width: 1200px; height: 1200px; overflow: hidden; background: var(--backdrop); }
  body { position: relative; font-family: "Oswald", sans-serif; color: var(--ink); }
  .sheet { position: absolute; left: 278px; top: 153px; width: 633px; height: 895px; background: var(--paper); overflow: hidden; }
  .abs { position: absolute; }
  .art { position: absolute; border-radius: 8px; background: linear-gradient(160deg, var(--red-soft), var(--red)); opacity: .55; }
  .menu-title { left: 0; width: 633px; top: 34px; text-align: center; font-family: "Anton", sans-serif; font-size: 62px; letter-spacing: 6px; line-height: 1; }
  .tagline-strip { left: 0; width: 633px; top: 99px; text-align: center; font-size: 7px; font-weight: 500; letter-spacing: .3px; white-space: nowrap; }
  .header-rule { left: 46px; top: 117px; width: 546px; height: 2px; background: var(--ink); }
  .section-title { font-family: "Anton", sans-serif; font-weight: 400; line-height: 1; letter-spacing: 1px; }
  .section-note { font-size: 8px; font-weight: 500; text-align: center; line-height: 1.3; }
  .price-line { font-weight: 500; text-align: center; white-space: nowrap; }
  .frame { position: absolute; border-left: 2px solid var(--ink); border-bottom: 2px solid var(--ink); }
  .item { position: absolute; }
  .item-name { font-size: 13px; font-weight: 600; letter-spacing: .8px; line-height: 1.1; text-transform: uppercase; }
  .item-desc { font-size: 6.3px; font-weight: 500; letter-spacing: .3px; text-transform: uppercase; line-height: 1.35; }
  .toppings-title { left: 0; width: 310px; top: 428px; text-align: center; font-family: "Dancing Script", cursive; font-size: 40px; }
  .topping-row { position: absolute; left: 46px; width: 194px; display: flex; justify-content: space-between; font-size: 13px; font-weight: 600; letter-spacing: .6px; white-space: nowrap; }
  .big-head { font-family: "Anton", sans-serif; font-size: 50px; line-height: 1; letter-spacing: -1px; transform: scaleX(.82); transform-origin: left top; white-space: nowrap; }
  .head-tag { font-size: 6.5px; letter-spacing: .2px; white-space: nowrap; }
  .row { position: absolute; display: flex; justify-content: space-between; font-size: 11.5px; font-weight: 600; letter-spacing: .6px; line-height: 1; }
  .row-desc { position: absolute; font-size: 6px; line-height: 1.3; }
  .box { position: absolute; top: 611px; height: 206px; border: 2px solid var(--ink); border-top: none; }
  .brand-mark { left: 298px; width: 316px; top: 506px; text-align: center; font-family: "Anton", sans-serif; font-size: 54px; letter-spacing: 2px; color: var(--yellow); }
  .footer { left: 0; width: 633px; top: 850px; display: flex; justify-content: center; align-items: center; gap: 18px; font-size: 14px; font-weight: 600; }
  .social { display: flex; align-items: center; gap: 4px; font-size: 17px; }
  .social-dot { width: 16px; height: 16px; border-radius: 50%; background: var(--red); }
</style>
</head>
<body>
<main class="sheet">
  <div class="art" style="left:68px;top:56px;width:158px;height:34px" role="img" aria-label="Row of sketched fast food: drinks, fries, burger, hotdog"></div>
  <div class="art" style="left:414px;top:56px;width:158px;height:34px" role="img" aria-label="Row of sketched fast food: hotdog, burger, fries, drinks"></div>
  <h1 class="abs menu-title">MENU</h1>
  <p class="abs tagline-strip">WURMELO FAST FOOD · HOT DOGS · BURGERS · FRIES · WURMELO FAST FOOD · HOT DOGS · BURGERS · FRIES · WURMELO FAST FOOD · HOT DOGS · BURGERS · FRIES ·</p>
  <div class="abs header-rule"></div>

  <!-- Hotdogs -->
  <section>
    <h2 class="abs section-title" style="left:0;width:330px;top:138px;font-size:25px;text-align:center">HOTDOGS</h2>
    <p class="abs section-note" style="left:0;width:330px;top:165px">OUR SPECIAL FRESH GRILLED HOTDOG SERVED ON FRESH BUNS</p>
    <p class="abs price-line" style="left:38px;width:252px;top:176px;font-size:11px;letter-spacing:.3px">-REGULAR – 1.300 OMR / FRANKS – 2.000 OMR-</p>
    <div class="frame" style="left:36px;top:190px;width:256px;height:222px;border-bottom:none"></div>
    <div class="abs" style="left:36px;top:410px;width:150px;height:2px;background:var(--ink)"></div>
    <div class="abs" style="left:290px;top:297px;width:2px;height:115px;background:var(--ink)"></div>
    <div class="art" style="left:214px;top:194px;width:134px;height:88px" role="img" aria-label="Sketch of a loaded hotdog in a bun"></div>
    <div class="item" style="left:46px;top:206px"><div class="item-name">Wurmelo</div><div class="item-desc">Lettuce, tomato, jalapeno, pickle, onion, corn,<br>chips, cheese, ketchup, mayo, mustard</div></div>
    <div class="item" style="left:46px;top:248px"><div class="item-name">Pepper</div><div class="item-desc">Bell pepper, onion, sweet chili sauce, avocado</div></div>
    <div class="item" style="left:46px;top:278px"><div class="item-name">Chili Flames</div><div class="item-desc">Chili carne, cheddar cheese, honey mustard</div></div>
    <div class="item" style="left:46px;top:305px"><div class="item-name">Chicago</div><div class="item-desc">Tomato, pickle, red onion, sweet relish, mustard</div></div>
    <div class="item" style="left:46px;top:333px"><div class="item-name">New York</div><div class="item-desc">Grilled onion, beef bacon, barbecue sauce, chili mustard</div></div>
    <div class="item" style="left:46px;top:365px"><div class="item-name">Egg &amp; Cheese</div><div class="item-desc">Omelet, cheese, ketchup, mayo, mustard</div></div>
  </section>

  <!-- Burgers -->
  <section>
    <h2 class="abs section-title" style="left:330px;width:290px;top:129px;font-size:27px;text-align:center">BURGERS</h2>
    <p class="abs section-note" style="left:330px;width:290px;top:157px">100% ALL NATURAL BEEF &amp; FRESHLY GROUNDED,<br>100 GRAMS EACH PATTY SERVED ON FRESH BUNS.</p>
    <p class="abs price-line" style="left:334px;width:286px;top:182px;font-size:10px;letter-spacing:.2px">-SINGLE PATTY - 2.000 OMR / DOUBLE PATTY - 2.500 OMR-</p>
    <div class="abs" style="left:565px;top:199px;width:35px;height:2px;background:var(--ink)"></div>
    <div class="abs" style="left:598px;top:199px;width:2px;height:115px;background:var(--ink)"></div>
    <div class="abs" style="left:351px;top:340px;width:2px;height:28px;background:var(--ink)"></div>
    <div class="abs" style="left:351px;top:366px;width:150px;height:2px;background:var(--ink)"></div>
    <div class="item" style="left:360px;top:202px"><div class="item-name">Sweet Beef Burger</div><div class="item-desc">Beef bacon, cheese, lettuce, tomato, pickle.</div></div>
    <div class="item" style="left:360px;top:237px"><div class="item-name">Cheese Beef Burger</div><div class="item-desc">Cheese, pickle, Wurmelo sauce.</div></div>
    <div class="item" style="left:360px;top:273px"><div class="item-name">Mexican Beef Burger</div><div class="item-desc">Guacamole sauce, red onion, lettuce, tomato, Wurmelo sauce.</div></div>
    <div class="item" style="left:360px;top:309px"><div class="item-name">Chicken Burger</div><div class="item-desc">Fried chicken patty, lettuce, tomato, ranch<br>sauce, Wurmelo sauce</div></div>
    <div class="art" style="left:514px;top:314px;width:96px;height:88px" role="img" aria-label="Sketch of a stacked burger"></div>
  </section>

  <!-- Toppings -->
  <section>
    <div class="frame" style="left:36px;top:427px;width:256px;height:174px"></div>
    <div class="abs" style="left:290px;top:433px;width:2px;height:168px;background:var(--ink)"></div>
    <h2 class="abs toppings-title" style="font-weight:500">Toppings</h2>
    <div class="topping-row" style="top:494px"><span>EXTRA VEGGIES</span><span>0.100 OMR</span></div>
    <div class="topping-row" style="top:516px"><span>EXTRA CHEESE</span><span>0.300 OMR</span></div>
    <div class="topping-row" style="top:538px"><span>EXTRA BEEF BACON</span><span>0.400 OMR</span></div>
    <div class="topping-row" style="top:560px"><span>EXTRA PATTY</span><span>0.500 OMR</span></div>
    <div class="art" style="left:248px;top:486px;width:34px;height:96px" role="img" aria-label="Small sketches of onion, cheese, bacon and patty"></div>
  </section>

  <div class="art" style="left:310px;top:408px;width:292px;height:172px" role="img" aria-label="Sketch of a burger, hotdog and fries together"></div>
  <div class="abs brand-mark">WURMELO</div>

  <!-- Fries -->
  <section class="box" style="left:34px;width:184px">
    <h2 class="abs big-head" style="left:8px;top:11px">FRIES</h2>
    <p class="abs head-tag" style="left:8px;top:68px">FRESH, CRUNCHY AND DELICIOUS</p>
    <div class="art" style="left:112px;top:0;width:56px;height:72px" role="img" aria-label="Sketch of fries in a carton"></div>
    <div class="row" style="left:12px;width:158px;top:84px"><span>REGULAR……</span><span>0.600 OMR</span></div>
    <div class="row" style="left:12px;width:158px;top:100px"><span>CRISPY……</span><span>0.800 OMR</span></div>
    <div class="row" style="left:12px;width:158px;top:116px"><span>WEDGES……</span><span>0.800 OMR</span></div>
    <div class="row" style="left:12px;width:158px;top:134px"><span>CHILI FRIES</span><span>1.500 OMR</span></div>
    <p class="row-desc" style="left:12px;width:160px;top:146px">Topped with our chili carne, cheddar cheese, jalapeno, honey mustard</p>
    <div class="row" style="left:12px;width:158px;top:166px"><span>LAVA FRIES</span><span>1.500 OMR</span></div>
    <p class="row-desc" style="left:12px;width:160px;top:178px">Topped with fried bacon, fried onion, cheddar cheese, ranch sauce</p>
  </section>

  <!-- Sides -->
  <section class="box" style="left:228px;width:179px">
    <div class="art" style="left:10px;top:7px;width:54px;height:66px" role="img" aria-label="Sketch of nachos with dip"></div>
    <h2 class="abs big-head" style="left:70px;top:11px">SIDES</h2>
    <p class="abs head-tag" style="left:72px;top:66px">CRAZY TASTY ALSWAYS FRESH</p>
    <div class="row" style="left:8px;width:163px;top:90px"><span>CRISPY STRIPS</span><span>1.800 OMR</span></div>
    <p class="row-desc" style="left:8px;width:150px;top:102px;font-size:5px">5 pieces of chicken strips topped with BBQ sauce or honey mustard sauce, Wurmelo side sauce</p>
    <div class="row" style="left:8px;width:163px;top:121px"><span>JALAPENO CHEESE<br>BALLS</span><span>1.300 OMR</span></div>
    <p class="row-desc" style="left:8px;width:165px;top:145px;font-size:5px">6 pieces of jalapeno cheese balls, sweet chili side sauce</p>
    <div class="row" style="left:8px;width:163px;top:156px"><span>NACHOS</span><span>1.300 OMR</span></div>
    <p class="row-desc" style="left:8px;width:165px;top:168px;font-size:5px">A plate of nachos topped with cheddar cheese and jalapeno</p>
  </section>

  <!-- Drinks -->
  <section class="box" style="left:416px;width:184px">
    <div class="art" style="left:6px;top:7px;width:64px;height:74px" role="img" aria-label="Sketch of iced drinks with citrus"></div>
    <h2 class="abs big-head" style="left:76px;top:11px">DRINKS</h2>
    <p class="abs head-tag" style="left:78px;top:68px">REFRESHING AND DELICIOUS</p>
    <div class="row" style="left:12px;width:162px;top:95px;align-items:center"><span>FLAVORED<br>SPARKLING CANS</span><span>0.800 OMR</span></div>
    <div class="row" style="left:12px;width:162px;top:120px;align-items:flex-start"><span>FRESH ORANGE<br>JUICE</span><span>1.400 OMR</span></div>
    <div class="row" style="left:12px;width:162px;top:145px"><span>MINERAL WATER</span><span>0.300 OMR</span></div>
    <div class="row" style="left:12px;width:162px;top:161px"><span>SOFT DRINK</span><span>0.400 OMR</span></div>
    <div class="row" style="left:12px;width:162px;top:176px"><span>MOJITO</span><span>1.500 OMR</span></div>
  </section>

  <footer class="abs footer">
    <span>MUSCAT-OMAN -95550147</span>
    <span>AMMAN-JORDAN -0790000482</span>
    <span class="social"><span class="social-dot"></span>WURMELO.OFFICIAL</span>
  </footer>
</main>
</body>
</html>
```